Orthopaedic Clinic Needs facebook page

Orthopaedic Clinic needs facebook page. The name of our clinic is Maple & Ridge Orthopaedics. We focus on hip and knee orthopaedic conditions, as well as general orthopaedics. The main services are total knee replacements, total hip replacements, sports injury of the knee, hip fractures. Unique selling points of our service would be 1. Patient Centred Care, 2. Value Driven, 3. 2 Double-Fellowship Trained Surgeons.

Colour scheme should fit the logo design and be within the general colour recommendations of a medical clinic.

The design should be modern, eye catching, draws the end user to the website.

We would like to design our facebook page for future social media marketing.
In accordance with local advertisement regulations pertaining to medical clinics, no statements must have any information or laudatory statements such as the use of best, better, breakthrough, champions, or any statements that imply superiority and that may create unjustified expectations of services.

Target Market(s)

Patients
Friends family and relatives of patients.

Font styles to use
Serif
Sans Serif

Requirements
Must have
• My project must have my logo.

A nice colour scheme comfortable to the eye.
Nice to have
• Nice eye catching design that will draw the end user to the page.
Should not have
• Must not have any information that create unjustified expectaions.
Must not contain laudatory statements such as best, better, breakthrough, champions, or other statement that may create unjustified expecation of services.

```html
<!DOCTYPE html>
<html lang="en">
<head>
<meta charset="utf-8">
<title>Maple &amp; Ridge Orthopaedics – Cover</title>
<link rel="stylesheet" href="https://fonts.googleapis.com/css2?family=Questrial&family=Roboto+Condensed:wght@500&family=Roboto:wght@400;700&display=swap">
<style>
  :root {
    --bg-deep: #042a2f;
    --bg-mid: #0a4a4b;
    --bg-glow: #0f5e5b;
    --accent: #2ac4b6;
    --rule: #1f6f6d;
    --ring: #0b4443;
    --text: #ffffff;
    --text-soft: #d9e6e6;
    --tick: #6fb2ad;
    --photo-skin: #6b3f2a;
    --photo-red: #c6452f;
    --photo-bg: #c9c2b6;
  }
  * { margin: 0; padding: 0; box-sizing: border-box; }
  html, body { width: 1200px; height: 457px; overflow: hidden; background: var(--bg-deep); }
  .cover {
    position: relative;
    width: 1200px;
    height: 457px;
    overflow: hidden;
    background: radial-gradient(ellipse 620px 420px at 600px 228px, var(--bg-glow) 0%, var(--bg-mid) 45%, var(--bg-deep) 100%);
    font-family: "Questrial", sans-serif;
    color: var(--text);
  }
  .brand {
    position: absolute; left: 37px; top: 30px;
    display: flex; align-items: center; gap: 13px;
  }
  .brand-mark { width: 58px; height: 60px; background: var(--accent); border-radius: 4px; }
  .brand-name { font-size: 25px; line-height: 1.12; color: var(--text); width: 250px; }
  .rule { position: absolute; height: 3px; background: var(--rule); }
  .rule-brand { left: 37px; top: 102px; width: 311px; height: 2px; }
  .call {
    position: absolute; left: 35px; top: 109px;
    font-family: "Roboto", sans-serif; font-weight: 400; font-size: 23px; color: var(--text-soft);
  }
  .call strong { color: var(--accent); font-weight: 700; }
  .section-title {
    position: absolute;
    font-family: "Roboto Condensed", sans-serif; font-weight: 500; color: var(--accent);
  }
  .services-title { left: 35px; top: 177px; font-size: 30px; }
  .rule-services { left: 35px; top: 220px; width: 306px; }
  .list { position: absolute; list-style: none; }
  .list li { position: absolute; left: 0; display: flex; align-items: center; white-space: nowrap; }
  .list svg { flex: none; }
  .services { left: 36px; top: 0; }
  .services li { font-size: 24.5px; gap: 17px; }
  .services li svg { width: 24px; height: 24px; }
  .photo-ring {
    position: absolute; left: 417px; top: 45px; width: 366px; height: 366px;
    border-radius: 50%; background: var(--ring);
  }
  .photo {
    position: absolute; left: 428px; top: 56px; width: 344px; height: 344px; border-radius: 50%;
    background: radial-gradient(circle at 52% 48%, var(--photo-red) 0%, var(--photo-skin) 28%, #4b2a1e 50%, var(--photo-bg) 78%);
  }
  .usp-title { left: 811px; top: 92px; font-size: 45px; }
  .rule-usp { left: 811px; top: 156px; width: 355px; }
  .usps { left: 811px; top: 0; }
  .usps li { font-size: 32px; gap: 15px; align-items: flex-start; line-height: 36.6px; }
  .usps li svg { width: 24px; height: 24px; margin-top: 10px; }
</style>
</head>
<body>
<main class="cover">
  <div class="brand">
    <span class="brand-mark"></span>
    <span class="brand-name">Maple &amp; Ridge Orthopaedics</span>
  </div>
  <div class="rule rule-brand"></div>
  <p class="call">Call us at: <strong>+1-216-555-0148</strong></p>

  <h2 class="section-title services-title">Service We Offer</h2>
  <div class="rule rule-services"></div>
  <ul class="list services">
    <li style="top:244px"><svg viewBox="0 0 24 24" fill="none" stroke="var(--tick)" stroke-width="1.8" stroke-linecap="round" stroke-linejoin="round"><path d="M21 11a9 9 0 1 1-4-7.4"/><path d="M7.5 11.5l3.5 3.5L21.5 4.5"/></svg>Total Knee Replacements</li>
    <li style="top:290px"><svg viewBox="0 0 24 24" fill="none" stroke="var(--tick)" stroke-width="1.8" stroke-linecap="round" stroke-linejoin="round"><path d="M21 11a9 9 0 1 1-4-7.4"/><path d="M7.5 11.5l3.5 3.5L21.5 4.5"/></svg>Total Hip Replacements</li>
    <li style="top:335px"><svg viewBox="0 0 24 24" fill="none" stroke="var(--tick)" stroke-width="1.8" stroke-linecap="round" stroke-linejoin="round"><path d="M21 11a9 9 0 1 1-4-7.4"/><path d="M7.5 11.5l3.5 3.5L21.5 4.5"/></svg>Hip Fractures</li>
    <li style="top:382px"><svg viewBox="0 0 24 24" fill="none" stroke="var(--tick)" stroke-width="1.8" stroke-linecap="round" stroke-linejoin="round"><path d="M21 11a9 9 0 1 1-4-7.4"/><path d="M7.5 11.5l3.5 3.5L21.5 4.5"/></svg>Sports injury of the knee</li>
  </ul>

  <div class="photo-ring"></div>
  <div class="photo" role="img" aria-label="Photo of a runner holding a painful, reddened knee on outdoor stairs"></div>

  <h2 class="section-title usp-title">Our Unique Service</h2>
  <div class="rule rule-usp"></div>
  <ul class="list usps">
    <li style="top:178px"><svg viewBox="0 0 24 24" fill="none" stroke="var(--tick)" stroke-width="1.8" stroke-linecap="round" stroke-linejoin="round"><path d="M21 11a9 9 0 1 1-4-7.4"/><path d="M7.5 11.5l3.5 3.5L21.5 4.5"/></svg>Patient Centred Care</li>
    <li style="top:227px"><svg viewBox="0 0 24 24" fill="none" stroke="var(--tick)" stroke-width="1.8" stroke-linecap="round" stroke-linejoin="round"><path d="M21 11a9 9 0 1 1-4-7.4"/><path d="M7.5 11.5l3.5 3.5L21.5 4.5"/></svg>Value Driven</li>
    <li style="top:282px"><svg viewBox="0 0 24 24" fill="none" stroke="var(--tick)" stroke-width="1.8" stroke-linecap="round" stroke-linejoin="round"><path d="M21 11a9 9 0 1 1-4-7.4"/><path d="M7.5 11.5l3.5 3.5L21.5 4.5"/></svg><span>2 Double-Fellowship<br>Trained Surgeons</span></li>
  </ul>
</main>
</body>
</html>
```